Brightway Carpet and Tile cleaning Business card Design

I need a design that has the same feel as my van.
i would also like a prominent "Review us on facebook" somewhere, but not that it makes it look silly.
I would like the card to have a little bit of grey or black in the design as well.

It will need contact details
phone: 0498 716254
email: rkbrightwayclean@mailvista.com
website: www.brightwaycarpetandtilecleaning.com.au
facebook: /brightwaycarpetandtilecleaning

Industry/Entity Type

Business

Contact Information for Business Card

Phone number 0498716254
Email rkbrightwayclean@mailvista.com
Website www.brightwaycarpetandtilecleaning.com.au
Facebook/brightwaycarpetandtilecleaning

Colors
000000

Requirements
Must have
• Same feel as my van
• I want the card to stand out from the crowd
Nice to have
• Maybe include a tiny bit of a third colour? Grey's,blacks, orange?

```html
<!DOCTYPE html>
<html lang="en">
<head>
<meta charset="utf-8">
<title>Brightway Carpet and Tile cleaning – Business Cards</title>
<link rel="stylesheet" href="https://fonts.googleapis.com/css2?family=Arimo:wght@400;700&display=swap">
<style>
  :root {
    --stage: #2b2b2d;
    --card-dark: #3c3c3e;
    --card-light: #ffffff;
    --brand-blue: #1ba7dc;
    --accent-orange: #e8821e;
    --ink: #222222;
    --rule: #555555;
    --band-dark: #3a3a3a;
  }
  * { box-sizing: border-box; margin: 0; padding: 0; }
  html, body {
    width: 1200px; height: 900px; overflow: hidden;
    background: var(--stage);
    font-family: "Arimo", Arial, sans-serif;
  }
  .stage { position: relative; width: 1200px; height: 900px; }

  .card {
    position: absolute;
    width: 560px; height: 320px;
    border-radius: 18px;
    overflow: hidden;
    box-shadow: 0 18px 40px rgba(0,0,0,.45);
  }
  .card--back { left: 60px; top: 90px; background: var(--card-dark); }
  .card--front { left: 580px; top: 490px; background: var(--card-light); }

  .brand {
    position: absolute; left: 0; right: 0;
    display: flex; align-items: center; justify-content: center; gap: 12px;
  }
  .brand__dot {
    width: 30px; height: 30px; border-radius: 50%;
    background: var(--brand-blue);
  }
  .brand__name {
    font-size: 44px; font-weight: 700; color: var(--brand-blue);
    letter-spacing: -0.5px; white-space: nowrap;
  }
  .card--back .brand { top: 110px; }
  .card--front .brand { top: 36px; }
  .card--front .brand__name { font-size: 40px; }

  .review-cta {
    position: absolute; right: 36px; bottom: 40px;
    color: #fff; font-weight: 700; font-size: 17px; letter-spacing: 2.5px;
    white-space: nowrap;
  }

  .band {
    position: absolute; left: 0; right: 0; bottom: 0; height: 16px;
    display: flex;
  }
  .band span { display: block; height: 100%; }
  .band .blue { background: var(--brand-blue); }
  .band .white { background: #fff; }
  .band .orange { background: var(--accent-orange); }
  .band .dark { background: var(--band-dark); }

  .name-row {
    position: absolute; top: 118px; left: 0; right: 0;
    display: flex; align-items: center; gap: 12px;
  }
  .name-row .rule { flex: 1; height: 2px; background: var(--rule); }
  .holder-name {
    color: var(--brand-blue); font-size: 24px; font-weight: 400; letter-spacing: 2px;
  }
  .icons {
    position: absolute; top: 154px; left: 0; right: 0;
    display: flex; justify-content: center; gap: 6px;
  }
  .icons svg { width: 12px; height: 12px; }
  .contact {
    position: absolute; top: 174px; left: 0; right: 0;
    list-style: none; text-align: center;
    color: var(--ink); font-size: 14px; line-height: 19px;
    white-space: nowrap;
  }
  .base-rule {
    position: absolute; left: 0; right: 0; top: 268px; height: 2px; background: var(--rule);
  }
</style>
</head>
<body>
<main class="stage">

  <section class="card card--back" aria-label="Business card back">
    <div class="brand">
      <span class="brand__dot"></span>
      <span class="brand__name">Brightway Clean</span>
    </div>
    <p class="review-cta">REVIEW US ON CHATTERLY</p>
    <div class="band">
      <span class="blue" style="width:45%"></span>
      <span class="white" style="width:30%"></span>
      <span class="orange" style="width:25%"></span>
    </div>
  </section>

  <section class="card card--front" aria-label="Business card front">
    <div class="brand">
      <span class="brand__dot"></span>
      <span class="brand__name">Brightway Clean</span>
    </div>

    <div class="name-row">
      <span class="rule"></span>
      <h1 class="holder-name">RICKY</h1>
      <span class="rule"></span>
    </div>

    <div class="icons" aria-hidden="true">
      <svg viewBox="0 0 12 12"><path d="M2.5 1h2l1 2.6-1.3 1a6 6 0 0 0 3.2 3.2l1-1.3L11 7.5v2c0 .8-.7 1.5-1.5 1.5A8.5 8.5 0 0 1 1 2.5C1 1.7 1.7 1 2.5 1z" fill="var(--brand-blue)"/></svg>
      <svg viewBox="0 0 12 12"><rect x="1" y="2.5" width="10" height="7" rx="1" fill="var(--brand-blue)"/><path d="M1.5 3l4.5 3.5L10.5 3" stroke="#fff" stroke-width="1" fill="none"/></svg>
      <svg viewBox="0 0 12 12"><circle cx="6" cy="6" r="5" fill="var(--brand-blue)"/><path d="M1 6h10M6 1c-2 2.8-2 7.2 0 10M6 1c2 2.8 2 7.2 0 10" stroke="#fff" stroke-width=".8" fill="none"/></svg>
      <svg viewBox="0 0 12 12"><circle cx="6" cy="6" r="5" fill="var(--brand-blue)"/></svg>
    </div>

    <ul class="contact">
      <li>0498716254</li>
      <li>rkbrightwayclean@mailvista.com</li>
      <li>www.brightwaycarpetandtilecleaning.com</li>
      <li>Chatterly/brightwaycarpetandtilecleaning</li>
    </ul>

    <div class="base-rule"></div>
    <div class="band">
      <span class="blue" style="width:50%"></span>
      <span class="dark" style="width:30%"></span>
      <span class="orange" style="width:20%"></span>
    </div>
  </section>

</main>
</body>
</html>
```